IG ad to attract older men for better health #1

I want a bold headline Instagram Ad that coordinate with my website design with a racy sexy woman to attract men 45yrs old plus. See Two samples attached

Target Market(s)

Men 45 years old and older

Industry/Entity Type

Health And Wellness

Requirements
Must have
• eye catching appeal to men
Nice to have
• The copy to read
Kestrel61go is the headline at the top of the page. Then the copy reads...
"I want to seduce you to better health with a little T&A. Remove the excuses, provide ridiculously simple tips and advice to get you started on a path of lasting heath." Want more?

```html
<!DOCTYPE html>
<html lang="en">
<head>
<meta charset="UTF-8">
<title>Kestrel61go – Instagram Ad</title>
<link href="https://fonts.googleapis.com/css2?family=Audiowide&family=Saira+Condensed:wght@300;400&family=Arimo:wght@400&display=swap" rel="stylesheet">
<style>
  :root {
    --page-bg: #eeeeee;
    --ad-bg: #121212;
    --ad-bg-edge: #060606;
    --neon-yellow: #f7c928;
    --neon-yellow-glow: rgba(255, 196, 0, 0.75);
    --neon-red: #ff3a3f;
    --neon-red-glow: rgba(255, 20, 30, 0.8);
    --band-red: #e3242b;
    --button-yellow: #fcd100;
    --button-text: #e3242b;
    --white: #ffffff;
    --photo-skin: #b86a45;
    --photo-red: #d81e23;
    --photo-hair: #3a2018;
  }
  * { margin: 0; padding: 0; box-sizing: border-box; }
  html, body {
    width: 1200px;
    height: 1000px;
    overflow: hidden;
    background: var(--page-bg);
  }
  .ad {
    position: absolute;
    left: 207px;
    top: 107px;
    width: 786px;
    height: 786px;
    background: radial-gradient(ellipse at 60% 40%, var(--ad-bg) 0%, var(--ad-bg-edge) 100%);
    overflow: hidden;
  }
  .model-photo {
    position: absolute;
    left: 32px;
    top: 29px;
    width: 345px;
    height: 757px;
    border-radius: 140px 140px 0 0;
    background: linear-gradient(180deg,
      var(--photo-hair) 0%,
      var(--photo-skin) 30%,
      var(--photo-red) 55%,
      var(--photo-skin) 78%,
      #8e4e33 100%);
    opacity: 0.9;
  }
  .headline {
    position: absolute;
    right: 39px;
    top: 118px;
    font-family: "Audiowide", sans-serif;
    font-size: 62px;
    line-height: 1;
    color: var(--neon-yellow);
    text-shadow: 0 0 8px var(--neon-yellow-glow), 0 0 22px var(--neon-yellow-glow);
    white-space: nowrap;
  }
  .tagline {
    position: absolute;
    right: 29px;
    top: 246px;
    width: 460px;
    font-family: "Saira Condensed", sans-serif;
    font-weight: 300;
    font-size: 49px;
    line-height: 62px;
    text-align: right;
    text-transform: uppercase;
    color: #ffd9d9;
    text-shadow: 0 0 3px var(--neon-red), 0 0 10px var(--neon-red-glow), 0 0 20px var(--neon-red-glow);
  }
  .pitch-band {
    position: absolute;
    left: 302px;
    top: 454px;
    width: 484px;
    height: 115px;
    background: linear-gradient(90deg, rgba(227, 36, 43, 0.05) 0%, rgba(227, 36, 43, 0.65) 35%, var(--band-red) 100%);
  }
  .pitch-copy {
    position: absolute;
    right: 31px;
    top: 468px;
    width: 440px;
    font-family: "Arimo", Arial, sans-serif;
    font-size: 20.5px;
    line-height: 29px;
    text-align: right;
    color: var(--white);
  }
  .cta-button {
    position: absolute;
    left: 487px;
    top: 624px;
    width: 262px;
    height: 44px;
    border-radius: 22px;
    background: var(--button-yellow);
    display: flex;
    align-items: center;
    justify-content: center;
    font-family: "Audiowide", sans-serif;
    font-size: 23px;
    letter-spacing: 1px;
    color: var(--button-text);
  }
</style>
</head>
<body>
  <main class="ad">
    <div class="model-photo" role="img" aria-label="Photo of a woman in a red halter bodysuit and white cat-eye sunglasses, seen from behind, looking over her shoulder"></div>

    <h1 class="headline">Kestrel61go</h1>

    <p class="tagline">I want to seduce you<br>to better health with<br>a little T&amp;A.</p>

    <div class="pitch-band"></div>
    <p class="pitch-copy">Remove the excuses, provide ridiculously simple tips and advice to get you started on a path of lasting health.</p>

    <div class="cta-button">WANT MORE?</div>
  </main>
</body>
</html>
```